pasmuro.com

Develop a website for pasmura.com will be a site to sell tickets for concerts, shows, shows, theaters and others. I need a web design easy view, very easy to use and accumulate events by date. The aim is to develop the site was connected to a complex system that is already developed. (Important this page to a robust system was connected via links the idea is to develop only the front view)
Updates

Reason: I need more designs yet we have not made the decision

Target Market(s)

millennials, adults, who want to enjoy concerts and shows

Industry/Entity Type

Event

Number of Pages Required

5+ page

Colors
1b1b1b
aaaaaa
ffffff

Requirements
Must have
• Easy Vista, accumulation of upcoming events, past events. The tabs should have are: 1 Start: In this part of upcoming events occur. You could put a banner on the top and down the events by date. 2. How to order: page with instructions on how to purchase tickets 3. About Us: The company history 4. Contact: Phones and template for contact by mail 5. Our policies: shopping 6. Notice Privacy: Privacy Notice Copoy 7. Centers Sale: physical places where they can purchase tickets Promoters 8. access: Link to a template
Nice to have
• as you can see p www.volandrimexa.com or crunvía.com or crunvea.com or plovindex.com (important this page to a robust system was connected via links the idea is to develop only the front view)
Should not have
• Many things Tangled

```html
<!DOCTYPE html>
<html lang="es">
<head>
<meta charset="utf-8">
<title>pasmura.com — Registro</title>
<link href="https://fonts.googleapis.com/css2?family=Questrial&family=Source+Sans+3:wght@600;700&display=swap" rel="stylesheet">
<style>
  :root {
    --frame-light: #e4e4e4;
    --frame-mid: #b9b9b9;
    --bar-white: #ffffff;
    --nav-black: #1b1b1b;
    --nav-text: #e8e8e8;
    --brand-grey: #aaaaaa;
    --side-dark: #1a2327;
    --stage-top: #2c4580;
    --stage-mid: #2b3f78;
    --stage-low: #3a3f56;
    --field-white: #ffffff;
    --field-edge: #c58aa6;
    --label-white: #ffffff;
  }
  * { margin: 0; padding: 0; box-sizing: border-box; }
  html, body { width: 1200px; height: 1000px; overflow: hidden; }
  body {
    position: relative;
    background: linear-gradient(180deg, var(--frame-mid) 0%, var(--frame-light) 50%, var(--frame-mid) 100%);
    font-family: "Source Sans 3", "Myriad Pro", sans-serif;
  }
  .top-bar {
    position: absolute; left: 0; top: 137px; width: 1200px; height: 39px;
    background: var(--bar-white);
  }
  .main-nav {
    position: absolute; left: 93px; top: 141px; width: 726px; height: 35px;
    background: var(--nav-black);
  }
  .main-nav a {
    position: absolute; top: 8px;
    font-family: "Questrial", "Century Gothic", sans-serif;
    font-size: 15px; color: var(--nav-text); text-decoration: none;
  }
  .brand {
    position: absolute; left: 1016px; top: 146px;
    font-family: "Questrial", "Century Gothic", sans-serif;
    font-size: 17px; font-weight: 400; color: var(--brand-grey);
  }
  .page {
    position: absolute; left: 0; top: 176px; width: 1200px; height: 757px;
    background: var(--side-dark);
  }
  .stage-photo {
    position: absolute; left: 235px; top: 4px; width: 828px; height: 753px;
    background: radial-gradient(ellipse at 55% 45%, var(--stage-mid) 0%, var(--stage-top) 45%, var(--stage-low) 100%);
  }
  .signup-form { position: absolute; inset: 0; }
  .label {
    position: absolute; color: var(--label-white);
    font-weight: 700; font-size: 16px; line-height: 18px;
    letter-spacing: 0.2px; text-transform: uppercase;
  }
  .field {
    position: absolute; height: 30px;
    background: var(--field-white);
    border: 1px solid var(--field-edge); border-radius: 4px;
  }
  .choice {
    position: absolute; width: 54px; height: 30px;
    background: var(--field-white);
    color: #1b1b1b; font-weight: 700; font-size: 16px;
    display: flex; align-items: center; justify-content: center;
  }
</style>
</head>
<body>
  <div class="top-bar"></div>
  <nav class="main-nav">
    <a href="#" style="left:27px">Inico</a>
    <a href="#" style="left:115px">Comprar Boleto</a>
    <a href="#" style="left:298px">Quienes Somos</a>
    <a href="#" style="left:458px">Contacto</a>
    <a href="#" style="left:586px">Mi Cuenta</a>
  </nav>
  <div class="brand">pasmura.com</div>

  <main class="page">
    <div class="stage-photo" role="img" aria-label="Fotografía de acróbatas con trajes de lunares sobre un escenario, fondo azul"></div>

    <form class="signup-form">
      <span class="label" style="left:475px;top:79px">Nombre</span>
      <div class="field" style="left:563px;top:73px;width:247px"></div>

      <span class="label" style="left:472px;top:119px">Apellido</span>
      <div class="field" style="left:563px;top:113px;width:247px"></div>

      <span class="label" style="left:487px;top:169px">Sexo</span>
      <div class="choice" style="left:561px;top:162px">M</div>
      <div class="choice" style="left:628px;top:162px">F</div>

      <span class="label" style="left:462px;top:210px">Fecha de<br>Nacimiento</span>
      <div class="field" style="left:565px;top:213px;width:247px"></div>

      <span class="label" style="left:467px;top:271px">Correo Electronico</span>
      <div class="field" style="left:469px;top:294px;width:247px"></div>

      <span class="label" style="left:469px;top:339px">Cuidad</span>
      <div class="field" style="left:469px;top:369px;width:156px"></div>

      <span class="label" style="left:468px;top:409px">Direccion</span>
      <div class="field" style="left:466px;top:433px;width:311px"></div>

      <span class="label" style="left:467px;top:501px">Clave</span>
      <div class="field" style="left:466px;top:527px;width:311px"></div>

      <span class="label" style="left:464px;top:575px">Confirmacion de Clave</span>
      <div class="field" style="left:466px;top:600px;width:311px"></div>

      <span class="label" style="left:467px;top:638px">Usuario</span>
      <div class="field" style="left:466px;top:665px;width:311px"></div>
    </form>
  </main>
</body>
</html>
```